Junk Removal company with existing WordPress website needs new mobile enhanced website

I am looking to have someone take my existing website and either update it with a new design and menu which is more mobile enhanced (70% of my traffic is from mobile devices and most people stay on the home page to find what they need) or create a new website from scratch to achieve my design goals. My name goal is the have to home page be quick and easy to find what the customer is looking for.
Our current website is: BrightCreekJunkOut.com and Google my business page https://g.page/brightcreekjunkout
I have attached an example the design idea I came up with for the home page based on what I would like it to look like as well as some logo files and pictures.

```html
<!DOCTYPE html>
<html lang="en">
<head>
<meta charset="utf-8">
<title>Bright Creek Junk Out – Junk Removal &amp; Property Cleanouts</title>
<link href="https://fonts.googleapis.com/css2?family=Outfit:wght@400;500;600;700&family=Open+Sans:wght@400;600&display=swap" rel="stylesheet">
<style>
:root{
  --orange:#f7941d;
  --orange-dark:#e07d06;
  --ink:#1c1c1c;
  --text:#444;
  --muted:#888;
  --soft:#f6f6f9;
  --line:#e2e2e2;
  --night:#141414;
  --white:#fff;
}
*{box-sizing:border-box;margin:0;padding:0}
html,body{width:1200px;height:3924px;overflow:hidden}
body{font-family:"Open Sans",sans-serif;color:var(--text);background:var(--white);position:relative}
h1,h2,h3,.brand,.nav a,.btn{font-family:"Outfit",sans-serif}
.abs{position:absolute}
.btn{display:inline-block;background:var(--orange);color:var(--white);font-weight:600;border-radius:4px;text-decoration:none}
.btn-outline{display:inline-block;border:2px solid var(--orange);color:var(--ink);border-radius:20px;font-family:"Outfit",sans-serif;font-weight:500}

/* header */
.topbar{top:0;left:0;width:1200px;height:60px;background:var(--white)}
.topbar .call{left:120px;top:14px;font-size:11px;color:var(--muted);line-height:15px}
.topbar .call b{display:block;font-family:"Outfit",sans-serif;font-size:15px;color:var(--ink)}
.topbar .btn{right:120px;top:13px;font-size:13px;padding:9px 18px}
.nav{top:60px;left:0;width:1200px;height:30px;background:var(--night)}
.nav a{position:absolute;top:7px;color:var(--white);font-size:14px;text-decoration:none}
.brand-badge{left:530px;top:2px;width:140px;height:116px;background:var(--night);border:3px solid var(--orange);border-radius:14px;display:flex;flex-direction:column;align-items:center;justify-content:center;gap:6px}
.brand-badge .dot{width:28px;height:28px;border-radius:50%;background:var(--orange)}
.brand{color:var(--white);font-weight:700;font-size:15px;text-align:center;line-height:17px}

/* hero */
.hero{top:90px;left:0;width:1200px;height:730px;background:linear-gradient(180deg,#4f86cf 0%,#7faee3 45%,#9fb4a1 78%,#5c6e4c 100%)}
.hero h1{top:130px;width:1200px;text-align:center;color:var(--white);font-weight:500;font-size:44px}
.hero h1 strong{font-weight:700}
.hero .sub{top:190px;width:1200px;text-align:center;color:var(--white);font-family:"Outfit",sans-serif;font-size:18px}
.hero .btn{left:468px;top:246px;font-size:14px;padding:12px 26px}
.hero .trucks{left:80px;top:330px;width:1040px;height:400px;background:linear-gradient(180deg,rgba(240,240,240,.0),rgba(60,60,60,.35))}

/* intro */
.intro h2{left:192px;top:840px;font-size:26px;color:var(--ink);font-weight:600}
.intro .rule{left:192px;top:880px;width:40px;height:3px;background:var(--orange)}
.intro p{left:192px;top:900px;width:370px;font-size:13px;line-height:21px}
.intro .btn-outline{left:192px;top:1060px;font-size:13px;padding:7px 18px}
.intro .tag{left:588px;top:978px;background:var(--orange);color:var(--white);font-family:"Outfit",sans-serif;font-size:12px;padding:8px 12px;border-radius:3px;line-height:14px}

/* services */
.services{top:1220px;left:0;width:1200px;height:1480px;background:var(--soft)}
.services h2{top:60px;width:1200px;text-align:center;font-size:34px;font-weight:600;color:var(--ink)}
.services .lead{top:110px;width:1200px;text-align:center;font-size:13px;color:var(--muted)}
.service h3{font-size:27px;font-weight:600;color:var(--ink)}
.service .rule{width:40px;height:3px;background:var(--orange);margin:10px 0 24px}
.service ul{list-style:none;columns:2;column-gap:50px;font-size:12.5px;line-height:24px;width:400px}
.bubble{border-radius:50%;border:2px solid var(--orange);opacity:.5}

/* testimonials */
.quote-card{width:360px;height:170px;background:var(--white);box-shadow:0 6px 24px rgba(0,0,0,.08);padding:28px 30px 0 70px;font-size:12.5px;line-height:20px}
.quote-card .mark{position:absolute;left:28px;top:20px;font-family:"Outfit",sans-serif;font-size:54px;color:var(--orange);line-height:54px}
.reviewer{top:2990px;display:flex;align-items:center;gap:12px;font-size:11px;color:var(--muted)}
.reviewer .avatar{width:38px;height:38px;border-radius:50%;background:#b9b2a8}
.reviewer b{display:block;font-family:"Outfit",sans-serif;font-size:13px;color:var(--ink);letter-spacing:.5px}
.dots{top:3058px;left:584px;display:flex;gap:6px}
.dots i{width:6px;height:6px;border-radius:50%;background:var(--line)}
.dots i.on{background:var(--orange)}

/* contact */
.contact h2{top:3150px;width:1200px;text-align:center;font-size:32px;font-weight:700;color:var(--ink)}
.contact .lead{top:3200px;width:1200px;text-align:center;font-size:13px;line-height:19px;color:var(--text)}
.footer{top:3400px;left:0;width:1200px;height:524px;background:linear-gradient(180deg,#2a2a2a,var(--night) 40%)}
.form-card{left:190px;top:3262px;width:820px;height:300px;background:var(--white);border-top:3px solid var(--orange);box-shadow:0 8px 30px rgba(0,0,0,.15);padding:26px 40px}
.form-card h3{font-size:20px;font-weight:500;color:var(--ink);margin-bottom:14px}
.field{position:absolute;height:30px;border:1px solid var(--line);font-size:11px;color:#aaa;padding:8px 10px}
.form-card .btn{position:absolute;left:40px;top:258px;font-size:12px;padding:7px 24px}

/* footer */
.footer .brand-badge{left:190px;top:220px;width:130px;height:108px}
.footer p.about{left:190px;top:344px;width:260px;font-size:11.5px;line-height:18px;color:#bbb}
.footer h4{font-family:"Outfit",sans-serif;color:var(--white);font-size:14px;font-weight:600;letter-spacing:.5px}
.footer ul{list-style:none;font-size:12px;line-height:22px;color:#bbb;margin-top:10px}
.footer .sub-row{display:flex;margin-top:12px}
.footer .sub-row span{width:150px;height:26px;background:var(--white);font-size:11px;color:#999;padding:6px 8px}
.footer .sub-row b{width:50px;height:26px;background:var(--orange)}
.footer .social{display:flex;gap:8px;margin-top:14px}
.footer .social i{width:22px;height:22px;border-radius:50%;border:1px solid #bbb}
.footer .base{left:190px;top:480px;width:820px;border-top:1px solid #333;padding-top:12px;font-size:11px;color:#aaa;display:flex;justify-content:space-between}
</style>
</head>
<body>

<header>
  <div class="topbar abs">
    <div class="call abs">Call or text<b>(555) 014-2290</b></div>
    <a class="btn abs" href="#contact">Get Free Estimate</a>
  </div>
  <nav class="nav abs">
    <a href="#" style="left:190px">Home</a>
    <a href="#services" style="left:262px">Our Services</a>
    <a href="#" style="left:820px">What We Take</a>
    <a href="#contact" style="left:944px">Contact Us</a>
  </nav>
  <div class="brand-badge abs"><span class="dot"></span><span class="brand">Bright Creek<br>Junk Out</span></div>
</header>

<section class="hero abs">
  <div class="trucks abs" role="img" aria-label="Photo of three branded junk removal trucks parked on a lawn under a blue sky"></div>
  <h1 class="abs">Best Rated <strong>JUNK REMOVEL</strong></h1>
  <p class="sub abs">&amp; Property Cleanout Company in the Bright Creek Valley</p>
  <a class="btn abs" href="tel:5550142290">&#9990;&nbsp; CALL US NOW (555) 014-2290</a>
</section>

<section class="intro">
  <svg class="abs" style="left:0;top:860px" width="120" height="200" aria-hidden="true"><circle cx="0" cy="100" r="96" fill="var(--soft)"/></svg>
  <h2 class="abs">Junk Removal and Hauling</h2>
  <div class="rule abs"></div>
  <p class="abs">The Best Rated Junk Hauling and Cleanout Service in the Bright Creek area with fast Response time and Same Day &amp; Next Day service available. We're the Friendliest and Most Professional junk haulers serving Alder Falls, Pine Hollow, Redfield, Marrow, Linton, Westbrook, Cedar Ridge and all of the Valley. Call us Today | (555) 014-2290</p>
  <span class="btn-outline abs">Book Service Now</span>
  <svg class="abs" style="left:650px;top:780px" width="320" height="370" aria-hidden="true">
    <circle cx="270" cy="60" r="70" fill="var(--soft)"/>
    <polyline points="40,110 160,40 280,110" fill="none" stroke="var(--orange)" stroke-width="4"/>
  </svg>
  <svg class="abs" style="left:680px;top:800px" width="260" height="300" role="img" aria-label="Photo of a junk removal truck with a loaded trailer">
    <defs><linearGradient id="g1" x1="0" y1="0" x2="0" y2="1"><stop offset="0" stop-color="#8fb4de"/><stop offset="1" stop-color="#4d5a4a"/></linearGradient></defs>
    <polygon points="130,0 260,75 260,225 130,300 0,225 0,75" fill="url(#g1)"/>
  </svg>
  <div class="tag abs">&#128222; Free<br>Estimates</div>
</section>

<section class="services abs" id="services">
  <h2 class="abs">Our Services</h2>
  <p class="lead abs">Lorem Ipsum is simply dummy text of the printing and typesetting industry.</p>

  <svg class="abs" style="left:180px;top:140px" width="320" height="380" aria-hidden="true">
    <polyline points="20,260 20,110 70,80" fill="none" stroke="var(--orange)" stroke-width="4"/>
  </svg>
  <svg class="abs" style="left:210px;top:160px" width="260" height="300" role="img" aria-label="Photo of a yard piled with household junk and tires">
    <defs><linearGradient id="g2" x1="0" y1="0" x2="0" y2="1"><stop offset="0" stop-color="#6f8c4e"/><stop offset="1" stop-color="#5b5246"/></linearGradient></defs>
    <polygon points="130,0 260,75 260,225 130,300 0,225 0,75" fill="url(#g2)"/>
  </svg>
  <div class="bubble abs" style="left:390px;top:170px;width:20px;height:20px"></div>
  <div class="service abs" style="left:632px;top:250px">
    <h3>Junk Removal</h3><div class="rule"></div>
    <ul><li>Misc. Household Junk</li><li>Furniture Removal</li><li>Appliance Removal</li><li>Mattress Removal</li><li>Hot Tub Removal</li><li>Yard Debris Removal</li><li>Remodeling Debris</li><li>Construction Debris</li></ul>
  </div>

  <div class="service abs" style="left:256px;top:660px">
    <h3>Property Cleanouts</h3><div class="rule"></div>
    <ul><li>Estate Cleanout</li><li>Residential Cleanout</li><li>Garage Cleanout</li><li>Storage Unit Cleanout</li><li>Foreclosure Cleanout</li><li>Hoarder Cleanout</li><li>Attic Cleanout</li><li>Basement Cleanout</li></ul>
  </div>
  <div class="bubble abs" style="left:600px;top:610px;width:18px;height:18px"></div>
  <div class="bubble abs" style="left:630px;top:590px;width:12px;height:12px"></div>
  <svg class="abs" style="left:680px;top:600px" width="300" height="360" aria-hidden="true">
    <polyline points="270,200 270,290 220,320" fill="none" stroke="var(--orange)" stroke-width="4"/>
  </svg>
  <svg class="abs" style="left:690px;top:600px" width="260" height="300" role="img" aria-label="Photo of stacked cardboard moving boxes in a room">
    <defs><linearGradient id="g3" x1="0" y1="0" x2="0" y2="1"><stop offset="0" stop-color="#e9e4dc"/><stop offset="1" stop-color="#b98e5e"/></linearGradient></defs>
    <polygon points="130,0 260,75 260,225 130,300 0,225 0,75" fill="url(#g3)"/>
  </svg>

  <svg class="abs" style="left:180px;top:1020px" width="320" height="380" aria-hidden="true">
    <polyline points="20,250 20,330 80,360" fill="none" stroke="var(--orange)" stroke-width="4"/>
  </svg>
  <svg class="abs" style="left:210px;top:1040px" width="260" height="300" role="img" aria-label="Photo of an old wooden shed ready for tear down">
    <defs><linearGradient id="g4" x1="0" y1="0" x2="0" y2="1"><stop offset="0" stop-color="#dcdcdc"/><stop offset="1" stop-color="#5d5b50"/></linearGradient></defs>
    <polygon points="130,0 260,75 260,225 130,300 0,225 0,75" fill="url(#g4)"/>
  </svg>
  <div class="service abs" style="left:632px;top:1090px">
    <h3>Light Demolition &amp; Tear Down</h3><div class="rule"></div>
    <ul><li>Shed Removal</li><li>Fence Removal</li><li>Deck Removal</li><li>Hot Tub Removal</li><li>Play Structure Removal</li><li>Swing Set Removal</li><li>Gazebo Removal</li><li>Above Ground Pool</li></ul>
  </div>
</section>

<section class="testimonials">
  <div class="quote-card abs" style="left:190px;top:2790px"><span class="mark">&ldquo;</span>Lorem ipsum dolor sit amet, consectetur adipiscing elit. Nullam iaculis urna. Phasellus dictum at purus iaculis accumsan. Sed at pulvinar mi.</div>
  <div class="quote-card abs" style="left:650px;top:2750px"><span class="mark">&ldquo;</span>Lorem ipsum dolor sit amet, consectetur adipiscing elit. Nullam iaculis urna. Phasellus dictum at purus iaculis accumsan. Sed a pulvinar phasellus dolor in vestibulum. Vivamus eget finibus ipsum, quis pulvinar nibh.</div>
  <div class="reviewer abs" style="left:230px"><span class="avatar"></span><div><b>NORA CASTELL / OWNER</b>Castell Consulting Group</div></div>
  <div class="reviewer abs" style="left:630px"><span class="avatar"></span><div><b>OWEN PIKE / CO-FOUNDER</b>Pike Studio</div></div>
  <div class="dots abs"><i class="on"></i><i></i><i></i></div>
</section>

<footer class="footer abs">
  <div class="brand-badge abs"><span class="dot"></span><span class="brand">Bright Creek<br>Junk Out</span></div>
  <p class="about abs">Lorem ipsum dolor sit amet, consectetur adipiscing elit. Nullam iaculis urna. Phasellus dictum at purus iaculis accumsan.</p>
  <div class="abs" style="left:580px;top:236px"><h4>SITEMAP</h4><ul><li>Home</li><li>Our Services</li><li>What We Take</li><li>Sitemap</li><li>Contact</li></ul></div>
  <div class="abs" style="left:800px;top:236px"><h4>STAY IN TOUCH</h4><ul><li>Subscribe Our Newsletter</li></ul><div class="sub-row"><span>Your email</span><b></b></div><div class="social"><i></i><i></i><i></i><i></i></div></div>
  <div class="base abs"><span>&copy; 2024 Bright Creek Junk Out. All Rights Reserved</span><span>Privacy Policy &nbsp;|&nbsp; Faq &nbsp;|&nbsp; Terms</span></div>
</footer>

<section class="contact" id="contact">
  <h2 class="abs">CONTACT</h2>
  <p class="lead abs">Lorem ipsum dolor sit amet, consectetur adipiscing elit.<br>Nunc ac consectetur leo. Mauris vitae lacus.</p>
  <form class="form-card abs">
    <h3>Feel Free to Contact Us</h3>
    <span class="field" style="left:40px;top:70px;width:360px">First Name</span>
    <span class="field" style="left:420px;top:70px;width:360px">Last Name</span>
    <span class="field" style="left:40px;top:112px;width:360px">Email</span>
    <span class="field" style="left:420px;top:112px;width:360px">Subject</span>
    <span class="field" style="left:40px;top:154px;width:740px;height:90px">Message</span>
    <span class="btn">SUBMIT</span>
  </form>
</section>

</body>
</html>
```